Trendy eye catching business card for lawn mowing business

Verge Kings, a local community lawn mowing service, requires an eye catching trendy business card to drop into letterboxes.

We could simply throw something together from a Microsoft Word template, but we are wanting something more than this. Some other business’ images are attached for some inspiration.

We are requiring the card to have Verge Kings with our slogan, Call The Pembrys. In addition, provide details with that we are a local, affordable lawn mowing service, and for other gardening matters to simply just ask!
Plus the relevant contact details, phone, email, social media.

Target Market(s)

Local community members who require assistance with their garden care

Industry/Entity Type

Gardening

Contact Information for Business Card

the name VERGE KINGS is our logo
telephone logo 0438 215 967
email logo vergekings@postbox-demo.com
Instagram logo vergekings
Facebook logo vergekings.sth
Lawn Mowing Service
Local Affordable
edge trim, blow and clipping removal included.
Other gardening matters, just ask!

Font styles to use
Serif
Sans Serif
Decorative
Script

Colors
9bcb3c
ffffff

Requirements
Must have
• All the details listed in Business Card Details.
Make these words prominent:
Verge Kings
Lawn Mowing Service
Local
Affordable
Nice to have
• Our slogan ‘Call The Pembrys’ incorporated.
Different colour background for front and reverse side
Greens, white and black colours
Subtle grass blades images incorporated
Should not have
• No images of lawnmowers.
No images of men/cartoons.
No using initials for Verge Kings

```html
<!DOCTYPE html>
<html lang="en">
<head>
<meta charset="utf-8">
<title>Verge Kings – Business Card</title>
<link rel="stylesheet" href="https://fonts.googleapis.com/css2?family=Oswald:wght@700&family=Questrial&display=swap">
<style>
  :root {
    --page: #2a2a2a;
    --card: #1b1b1b;
    --card-edge: #141414;
    --green: #9bcb3c;
    --green-deep: #6aa83a;
    --white: #ffffff;
  }
  * { box-sizing: border-box; margin: 0; padding: 0; }
  html, body { width: 1200px; height: 1101px; overflow: hidden; }
  body {
    background: var(--page);
    display: flex;
    flex-direction: column;
    align-items: center;
    justify-content: center;
    gap: 40px;
    font-family: "Questrial", sans-serif;
    color: var(--white);
  }
  .card {
    position: relative;
    width: 860px;
    height: 490px;
    background: radial-gradient(ellipse at 60% 40%, #242424 0%, var(--card) 60%, var(--card-edge) 100%);
    overflow: hidden;
    box-shadow: 0 10px 30px rgba(0,0,0,.45);
  }
  .band { position: absolute; inset: 0; width: 100%; height: 100%; }

  /* contact side */
  .mini-logo {
    position: absolute;
    left: 50px; top: 0; height: 490px;
    writing-mode: vertical-rl;
    transform: rotate(180deg);
    display: flex; flex-direction: column; justify-content: center; align-items: center;
    gap: 6px;
    white-space: nowrap;
  }
  .mini-logo .name {
    font-family: "Oswald", sans-serif; font-weight: 700;
    font-size: 40px; line-height: 1; color: var(--white); letter-spacing: 1px;
  }
  .mini-logo .slogan { font-size: 12px; letter-spacing: 2px; color: var(--white); }
  .contacts {
    position: absolute; left: 370px; top: 150px;
    list-style: none; display: flex; flex-direction: column; gap: 16px;
    font-size: 25px; white-space: nowrap;
  }
  .contacts li { display: flex; align-items: center; gap: 12px; }
  .contacts .icon {
    width: 30px; height: 30px; border-radius: 50%;
    background: var(--green); flex: none;
    display: flex; align-items: center; justify-content: center;
  }

  /* logo side */
  .services {
    position: absolute; left: 40px; top: 0; height: 490px;
    writing-mode: vertical-rl;
    transform: rotate(180deg);
    display: flex; flex-direction: column; justify-content: center; align-items: center;
    gap: 2px;
    text-align: center;
    text-transform: uppercase;
    white-space: nowrap;
  }
  .services .headline { font-size: 24px; letter-spacing: .5px; }
  .services .tagline { font-size: 24px; color: var(--green); }
  .services .detail { font-size: 15px; }
  .brand {
    position: absolute; left: 420px; top: 110px; width: 400px;
    text-align: center;
  }
  .brand .name {
    font-family: "Oswald", sans-serif; font-weight: 700;
    font-size: 118px; line-height: 1; color: var(--white);
    text-transform: uppercase; letter-spacing: 2px;
  }
  .brand .slogan {
    margin-top: 14px; font-size: 24px; letter-spacing: 4px;
    text-transform: uppercase; color: var(--white);
  }
</style>
</head>
<body>

<section class="card card--contact">
  <svg class="band" viewBox="0 0 860 490" aria-hidden="true">
    <rect x="200" y="0" width="44" height="490" fill="var(--green)"/>
    <rect x="256" y="0" width="4" height="490" fill="var(--white)" opacity=".8"/>
  </svg>

  <div class="mini-logo">
    <span class="name">VERGE KINGS</span>
    <span class="slogan">CALL THE PEMBRYS</span>
  </div>

  <ul class="contacts">
    <li>
      <span class="icon">
        <svg width="16" height="16" viewBox="0 0 24 24" aria-hidden="true"><path fill="#1b1b1b" d="M6.6 10.8a15.1 15.1 0 0 0 6.6 6.6l2.2-2.2a1 1 0 0 1 1-.25 11.4 11.4 0 0 0 3.6.57 1 1 0 0 1 1 1V20a1 1 0 0 1-1 1A17 17 0 0 1 3 4a1 1 0 0 1 1-1h3.5a1 1 0 0 1 1 1c0 1.25.2 2.45.57 3.57a1 1 0 0 1-.25 1z"/></svg>
      </span>0438 215 967
    </li>
    <li>
      <span class="icon">
        <svg width="16" height="16" viewBox="0 0 24 24" aria-hidden="true"><path fill="#1b1b1b" d="M3 5h18v14H3z"/><path fill="none" stroke="#9bcb3c" stroke-width="2" d="M3 6l9 7 9-7"/></svg>
      </span>vergekings@postbox-demo.com
    </li>
    <li><span class="icon"></span>instagram.com/vergekings</li>
    <li><span class="icon"></span>fb.me/vergekings.sth</li>
  </ul>
</section>

<section class="card card--brand">
  <svg class="band" viewBox="0 0 860 490" aria-hidden="true">
    <rect x="300" y="0" width="44" height="490" fill="var(--green)"/>
    <rect x="356" y="0" width="4" height="490" fill="var(--white)" opacity=".8"/>
  </svg>

  <div class="services">
    <p class="headline">Lawn Mowing Service</p>
    <p class="tagline">Local. Affordable.</p>
    <p class="detail">Edge trim, blow and clipping removal included.</p>
    <p class="detail">Other gardening matters, just ask!</p>
  </div>

  <div class="brand">
    <p class="name">VERGE<br>KINGS</p>
    <p class="slogan">Call The Pembrys</p>
  </div>
</section>

</body>
</html>
```